Business Card Design Project

Front back design preferred. Vertical card, not horizontal. Logo being developed by your group.

Industry/Entity Type

Business

Font styles to use
Serif

Colors

Designer to choose colors to be used in the design.

Requirements
Must have
• Logo being developed by your designers. Normal names, titles, www address, phone numbers, email, offices.
Should not have
• Fax number!

```html
<!DOCTYPE html>
<html lang="en">
<head>
<meta charset="utf-8">
<title>Martin Hale – Business Card</title>
<link href="https://fonts.googleapis.com/css2?family=Bebas+Neue&family=Roboto:wght@400&display=swap" rel="stylesheet">
<style>
  :root {
    --card-dark: #242421;
    --accent-blue: #1f6e8c;
    --address-bar: #4e4b47;
    --ink-white: #ffffff;
    --page-bg: #ffffff;
  }
  html, body {
    margin: 0;
    padding: 0;
    width: 1200px;
    height: 1032px;
    overflow: hidden;
    background: var(--page-bg);
  }
  .sheet {
    position: relative;
    width: 1222px;
    height: 1050px;
    transform: scale(0.982);
    transform-origin: 0 0;
  }
  .card {
    position: absolute;
    top: 0;
    width: 600px;
    height: 1050px;
    overflow: hidden;
    background: var(--card-dark);
    color: var(--ink-white);
  }
  .card--front { left: 0; }
  .card--back { left: 622px; }

  .front__band {
    position: absolute; top: 0; bottom: 0;
    left: 32px; width: 76px;
    background: var(--accent-blue);
  }
  .front__band-line {
    position: absolute; top: 0; bottom: 0;
    left: 113px; width: 6px;
    background: var(--accent-blue);
  }
  .address-bar {
    position: absolute; left: 0; right: 0;
    top: 900px; height: 75px;
    background: var(--address-bar);
  }

  .brand {
    position: absolute;
    display: flex;
    align-items: center;
    gap: 10px;
    font-family: "Bebas Neue", sans-serif;
    line-height: 1;
    color: var(--ink-white);
  }
  .brand__square {
    display: block;
    background: var(--ink-white);
  }
  .brand--front { left: 273px; top: 122px; font-size: 50px; }
  .brand--front .brand__square { width: 40px; height: 40px; }
  .brand--back { left: 0; right: 0; justify-content: center; top: 392px; font-size: 84px; gap: 16px; }
  .brand--back .brand__square { width: 62px; height: 62px; }

  .person-name {
    position: absolute;
    margin: 0;
    font-family: "Bebas Neue", sans-serif;
    font-weight: 400;
    line-height: 1;
    letter-spacing: 0.5px;
  }
  .card--front .person-name { left: 212px; top: 254px; font-size: 66px; }
  .card--back .person-name { left: 0; right: 0; text-align: center; top: 566px; font-size: 68px; }

  .person-title {
    position: absolute;
    left: 212px; top: 315px;
    margin: 0;
    font-family: "Roboto", sans-serif;
    font-size: 17px;
    letter-spacing: 0.3px;
  }

  .contact {
    position: absolute;
    left: 162px;
    margin: 0;
    font-family: "Roboto", sans-serif;
    line-height: 1.3;
  }
  .contact--phone { top: 683px; font-size: 25px; letter-spacing: 0.5px; }
  .contact--web { top: 789px; font-size: 19px; }
  .contact--address { top: 925px; left: 161px; font-size: 19px; letter-spacing: 0.2px; }

  .icon {
    position: absolute;
    left: 56px;
    width: 32px;
    height: 32px;
    fill: var(--ink-white);
  }
  .icon--phone { top: 677px; }
  .icon--link { top: 802px; }
  .icon--pin { top: 922px; }

  .stripes {
    position: absolute;
    left: 0; width: 600px;
    height: 239px;
  }
  .stripes--top { top: 0; }
  .stripes--bottom { top: 811px; }
  .stripes span {
    position: absolute; top: 0; bottom: 0;
    background: var(--accent-blue);
  }
</style>
</head>
<body>
<div class="sheet">

  <section class="card card--front" aria-label="Card front">
    <div class="front__band"></div>
    <div class="front__band-line"></div>
    <div class="address-bar"></div>

    <div class="brand brand--front"><span class="brand__square"></span>HALE</div>

    <h1 class="person-name">Martin Hale</h1>
    <p class="person-title">GRAPHIC DESIGNER</p>

    <svg class="icon icon--phone" viewBox="0 0 24 24" aria-hidden="true">
      <path d="M6.6 10.8c1.4 2.8 3.8 5.1 6.6 6.6l2.2-2.2c.3-.3.7-.4 1-.2 1.1.4 2.3.6 3.6.6.6 0 1 .4 1 1V20c0 .6-.4 1-1 1C10.6 21 3 13.4 3 4c0-.6.4-1 1-1h3.5c.6 0 1 .4 1 1 0 1.3.2 2.5.6 3.6.1.3 0 .7-.2 1L6.6 10.8z"/>
    </svg>
    <p class="contact contact--phone">00-318-472-905</p>

    <svg class="icon icon--link" viewBox="0 0 24 24" aria-hidden="true">
      <path d="M12 4a8 8 0 0 1 7.4 5H22l-3.5 4-3.5-4h2.3A6 6 0 0 0 6.3 9.9L4.4 9.2A8 8 0 0 1 12 4zM12 20a8 8 0 0 1-7.4-5H2l3.5-4 3.5 4H6.7a6 6 0 0 0 11 -0.9l1.9.7A8 8 0 0 1 12 20z"/>
    </svg>
    <p class="contact contact--web">WWW.MARTINHALE.COM<br>martin.hale@MAILBOX.COM</p>

    <svg class="icon icon--pin" viewBox="0 0 24 24" aria-hidden="true">
      <path d="M12 2a7 7 0 0 0-7 7c0 5 7 13 7 13s7-8 7-13a7 7 0 0 0-7-7zm0 9.5A2.5 2.5 0 1 1 12 6.5a2.5 2.5 0 0 1 0 5z"/>
    </svg>
    <p class="contact contact--address">48 STUDIO LANE CEDAR CITY MICHIGAN</p>
  </section>

  <section class="card card--back" aria-label="Card back">
    <div class="stripes stripes--top">
      <span style="left:205px;width:6px"></span>
      <span style="left:216px;width:12px"></span>
      <span style="left:233px;width:18px"></span>
      <span style="left:256px;width:77px"></span>
      <span style="left:338px;width:17px"></span>
      <span style="left:360px;width:13px"></span>
      <span style="left:376px;width:7px"></span>
    </div>

    <div class="brand brand--back"><span class="brand__square"></span>HALE</div>
    <h2 class="person-name">Martin Hale</h2>

    <div class="stripes stripes--bottom">
      <span style="left:205px;width:6px"></span>
      <span style="left:216px;width:12px"></span>
      <span style="left:233px;width:18px"></span>
      <span style="left:256px;width:77px"></span>
      <span style="left:338px;width:17px"></span>
      <span style="left:360px;width:13px"></span>
      <span style="left:376px;width:7px"></span>
    </div>
  </section>

</div>
</body>
</html>
```